Business card design for a dynamic IT consulting company

We need a business card design for a young firm, specialized in the Telecommunications/Consulting industry. The name of the company is Brask and Partners Business Consulting Ltd. (Short name: Brask and Partnes)
Brask = solve read reverse, so we aim to be uncomplicated and solution-oriented. The small pipe in our logo is also related to the word solve. So we need a new business card design, which is simple, eye catching and something non traditional (I would probably prefer a square shaped design rather than a rectangle, but open for suggestions). Attached our logo.

Target Market(s)

Usually our customers are Tier1 Telecoms providers (Q-Linkra, Parnexo, etc) and their executives.

Industry/Entity Type

Business

Contact Information for Business Card

Name: Gergely Halmindo
Email: g.halmindo@braskpartnera.hu
Web: www.braskpartnera.hu
Mobile: +36 30 555 0192
Title: Managing Director

Optional:
Company name: Brask and Partners Ltd.
Address: 1047 Budapest, Ravaszi str. 17/B, Hungary

Font styles to use
Other font styles liked:
• helveticaneue_medium, Prime Regular are used now.

Colors

Designer to choose colors to be used in the design.

Requirements
Must have
• I would like to have a 2 sided design.
Nice to have
• I thought if we make the logo a bit bigger (without the company name), that could go to the back with the company name below. I though, if the pipe in the logo is somehow touchable on the business card, would be nice and unique.

```html
<!DOCTYPE html>
<html lang="en">
<head>
<meta charset="utf-8">
<title>Brask and Partners – Business Card</title>
<link href="https://fonts.googleapis.com/css2?family=Roboto:wght@300;400;500;700&display=swap" rel="stylesheet">
<style>
  :root {
    --backdrop: #9b9b9b;
    --paper: #ffffff;
    --ink: #1e1e1e;
    --ink-soft: #333333;
    --brand-grey: #5d5e60;
    --magenta: #b83293;
    --cyan: #0a9bd9;
    --reverse: #000000;
  }
  * { box-sizing: border-box; margin: 0; padding: 0; }
  html, body {
    width: 1200px; height: 1200px; overflow: hidden;
    background: var(--backdrop);
    font-family: "Roboto", Arial, sans-serif;
  }
  .card {
    position: absolute; left: 135px; width: 930px; height: 531px; overflow: hidden;
  }
  .card--front { top: 44px; background: var(--paper); }
  .card--back { top: 600px; background: var(--reverse); }

  .brand-name {
    position: absolute; left: 37px; top: 226px;
    font-size: 42px; font-weight: 400; color: var(--brand-grey);
    display: flex; align-items: center; gap: 14px; letter-spacing: 0.5px;
  }
  .brand-name__square { width: 22px; height: 22px; background: var(--magenta); }

  .band {
    position: absolute; display: flex; align-items: center; justify-content: flex-end;
    color: #fff; font-weight: 700; padding-right: 25px; white-space: nowrap;
  }
  .band--name {
    left: 514px; top: 235px; width: 416px; height: 48px;
    background: var(--magenta); font-size: 34px; letter-spacing: -0.3px;
    clip-path: polygon(0 0, 100% 0, 100% 100%, 30px 100%);
    padding-right: 18px;
  }
  .band--name .surname { font-weight: 300; margin-left: 10px; }
  .band--title {
    left: 653px; top: 288px; width: 260px; height: 29px;
    background: var(--brand-grey); font-size: 16px; justify-content: center;
    clip-path: polygon(0 0, 100% 0, calc(100% - 12px) 100%, 16px 100%);
  }
  .title-stripe { position: absolute; top: 288px; height: 29px; width: 20px; }
  .title-stripe--cyan { left: 648px; background: var(--cyan); clip-path: polygon(0 0, 6px 0, 20px 100%, 14px 100%); }
  .title-stripe--magenta { left: 905px; background: var(--magenta); clip-path: polygon(0 0, 6px 0, 20px 100%, 14px 100%); }
  .band--phone {
    left: 685px; top: 338px; width: 245px; height: 37px;
    background: var(--cyan); font-size: 22px;
    clip-path: polygon(0 0, 100% 0, 100% 100%, 22px 100%);
  }
  .band--email {
    left: 548px; top: 381px; width: 382px; height: 37px;
    background: var(--magenta); font-size: 22px;
    clip-path: polygon(0 0, 100% 0, 100% 100%, 22px 100%);
  }
  .band--web {
    left: 640px; top: 426px; width: 290px; height: 38px;
    background: var(--brand-grey); font-size: 22px;
    clip-path: polygon(0 0, 100% 0, 100% 100%, 22px 100%);
  }

  .company {
    position: absolute; left: 35px; top: 368px; color: var(--ink);
  }
  .company__name { font-size: 32px; font-weight: 700; letter-spacing: -0.2px; }
  .company__address { margin-top: 6px; font-size: 18px; font-weight: 400; line-height: 23px; color: var(--ink-soft); }

  .back-brand {
    position: absolute; left: 0; right: 0; top: 0; bottom: 0;
    display: flex; align-items: center; justify-content: center; gap: 18px;
    color: #fff; font-size: 44px; font-weight: 400; letter-spacing: 0.5px;
  }
  .back-brand__square { width: 26px; height: 26px; background: var(--cyan); }
</style>
</head>
<body>
  <section class="card card--front">
    <div class="brand-name"><span class="brand-name__square"></span>Brask &amp; Partners</div>

    <div class="band band--name">GERGELY<span class="surname">HALMINDO</span></div>
    <span class="title-stripe title-stripe--cyan"></span>
    <div class="band band--title">MANAGING DIRECTOR</div>
    <span class="title-stripe title-stripe--magenta"></span>
    <div class="band band--phone">+36 30 555 0192</div>
    <div class="band band--email">g.halmindo@braskpartnera.hu</div>
    <div class="band band--web">www.braskpartnera.hu</div>

    <div class="company">
      <p class="company__name">Brask and Partners Ltd.</p>
      <p class="company__address">1047 Budapest, Ravaszi str.<br>17/B, Hungary</p>
    </div>
  </section>

  <section class="card card--back">
    <div class="back-brand"><span class="back-brand__square"></span>Brask &amp; Partners</div>
  </section>
</body>
</html>
```